Redesign our business card for more impact

We want to completely replace the back design of our card, and refresh or even change the front entirely. We are happy with our black Q7 logo and do not want to change it.
Our company address changed too. It is now 58 Corvallen, Irvine, CA 92741
Updates

It was reported by Sketch Harbor email today that the uploaded files didnt upload. I am trying again.

Target Market(s)

Architects and Building Owners (People making multi-million dollar decisions)

Industry/Entity Type

Consulting Engineering

Contact Information for Business Card

Contact info on the front. "wallpaper" design on back with tag line on the back "Engineering Your Future"

Font styles to use
Sans Serif

Requirements
Must have
• A vivid, modern, impactful ...but tasteful back of card design. It should communicate our premier status, but grab attention as innovative. DESIGN SHOULD BE ELEGANT AND NOT TOO BUSY.
Nice to have
• Repeating pattern, multi-color, something creative...
Should not have
• Anything that looks too playful or that we are not serious professionals. It should also not be too boring or conservative.

```html
<!DOCTYPE html>
<html lang="en">
<head>
<meta charset="utf-8">
<title>Q7 Engineering – Business Card</title>
<link href="https://fonts.googleapis.com/css2?family=Krona+One&family=Michroma&family=Montserrat:wght@700&display=swap" rel="stylesheet">
<style>
  :root {
    --page-bg: #ebebeb;
    --card-dark: #111111;
    --card-dark-sheen: #1d1d1d;
    --brand-red: #cc161b;
    --ink-dark: #333333;
    --paper: #ffffff;
    --rule: #5a5a5a;
  }
  html, body {
    margin: 0;
    padding: 0;
    width: 984px;
    height: 1200px;
    overflow: hidden;
    background: var(--page-bg);
  }
  .sheet {
    position: relative;
    width: 984px;
    height: 1200px;
  }
  .card {
    position: absolute;
    left: 113px;
    width: 758px;
    height: 433px;
    box-shadow: 0 6px 22px rgba(0, 0, 0, 0.35);
    display: block;
  }
  .card--logo-side { top: 121px; }
  .card--contact-side { top: 645px; }

  .wordmark {
    font-family: "Krona One", sans-serif;
    text-anchor: middle;
  }
  .wordmark--front { fill: var(--paper); font-size: 230px; }
  .wordmark--back { fill: var(--ink-dark); font-size: 124px; text-anchor: start; }

  .site-url {
    font-family: "Michroma", sans-serif;
    font-size: 30px;
    letter-spacing: 12px;
    fill: var(--paper);
    text-anchor: middle;
  }
  .site-url__domain { font-family: "Krona One", sans-serif; font-size: 33px; }

  .tagline {
    font-family: "Krona One", sans-serif;
    font-size: 60px;
    fill: var(--ink-dark);
  }
  .tagline__accent { fill: var(--brand-red); }

  .person-name {
    font-family: "Krona One", sans-serif;
    font-size: 47px;
    fill: var(--brand-red);
  }
  .person-title {
    font-family: "Montserrat", sans-serif;
    font-weight: 700;
    font-size: 25px;
    fill: var(--paper);
  }
  .contact-text {
    font-family: "Michroma", sans-serif;
    font-size: 28px;
    fill: var(--paper);
  }
  .contact-badge__ring { fill: var(--brand-red); }
  .contact-badge__core { fill: var(--paper); }
  .contact-badge__icon { fill: none; stroke: var(--ink-dark); stroke-width: 3; stroke-linecap: round; stroke-linejoin: round; }
  .contact-badge__icon--solid { fill: var(--ink-dark); stroke: none; }
  .divider { stroke: var(--rule); stroke-width: 2; }
  .band { fill: var(--brand-red); }
  .band-gap { fill: var(--card-dark); }
  .panel-light { fill: var(--paper); }
</style>
</head>
<body>
<main class="sheet">

  <!-- Logo side -->
  <svg class="card card--logo-side" viewBox="0 0 1156 660" aria-label="Q7 Engineering card, logo side">
    <defs>
      <linearGradient id="dark-sheen" x1="0" y1="1" x2="1" y2="0">
        <stop offset="0" stop-color="var(--card-dark)"/>
        <stop offset="0.5" stop-color="var(--card-dark-sheen)"/>
        <stop offset="1" stop-color="var(--card-dark)"/>
      </linearGradient>
    </defs>
    <rect width="1156" height="660" fill="url(#dark-sheen)"/>
    <text class="wordmark wordmark--front" x="578" y="443">Q7</text>

    <g class="url-band">
      <rect class="band" x="0" y="552" width="1156" height="53"/>
      <g class="band-gap">
        <polygon points="118,552 136,552 94,605 76,605"/>
        <polygon points="156,552 174,552 132,605 114,605"/>
        <polygon points="194,552 212,552 170,605 152,605"/>
        <polygon points="232,552 250,552 208,605 190,605"/>
        <polygon points="270,552 288,552 246,605 228,605"/>
        <polygon points="958,552 976,552 934,605 916,605"/>
        <polygon points="996,552 1014,552 972,605 954,605"/>
        <polygon points="1034,552 1052,552 1010,605 992,605"/>
        <polygon points="1072,552 1090,552 1048,605 1030,605"/>
        <polygon points="1110,552 1128,552 1086,605 1068,605"/>
      </g>
      <text class="site-url" x="578" y="591">www.<tspan class="site-url__domain">q7eng</tspan>.com</text>
    </g>
  </svg>

  <!-- Contact side -->
  <svg class="card card--contact-side" viewBox="0 0 1156 660" aria-label="Q7 Engineering card, contact side">
    <defs>
      <linearGradient id="dark-sheen-2" x1="0" y1="1" x2="1" y2="0">
        <stop offset="0" stop-color="var(--card-dark)"/>
        <stop offset="0.5" stop-color="var(--card-dark-sheen)"/>
        <stop offset="1" stop-color="var(--card-dark)"/>
      </linearGradient>
    </defs>
    <rect width="1156" height="660" fill="url(#dark-sheen-2)"/>

    <g class="header-panel">
      <polygon class="panel-light" points="0,0 1156,0 1156,262 436,262 397,313 0,313"/>
      <polygon class="band" points="0,252 432,252 390,304 0,304"/>
      <polygon class="band" points="620,201 1156,201 1156,256 578,256"/>
      <polygon class="band" points="470,201 492,201 450,256 428,256"/>
      <polygon class="band" points="508,201 530,201 488,256 466,256"/>
      <polygon class="band" points="546,201 568,201 526,256 504,256"/>
      <polygon class="band" points="584,201 606,201 564,256 542,256"/>
    </g>

    <text class="wordmark wordmark--back" x="60" y="186" textLength="205" lengthAdjust="spacing">Q7</text>

    <text class="tagline" x="306" y="103"><tspan class="tagline__accent">ENGINEERING</tspan> YOUR</text>
    <text class="tagline" x="306" y="166">FUTURE</text>

    <text class="person-name" x="58" y="388">Dana Whitcombe, PE</text>
    <text class="person-title" x="58" y="425">HFDP, LEED AP CEO/PRINCIPAL</text>
    <line class="divider" x1="58" y1="461" x2="1096" y2="461"/>

    <g class="contact contact--phone">
      <circle class="contact-badge__ring" cx="88" cy="510" r="27"/>
      <circle class="contact-badge__core" cx="88" cy="510" r="20"/>
      <path class="contact-badge__icon" d="M80 500 q-4 4 0 11 q5 9 13 12 q5 2 8 -2 l-5 -5 q-3 2 -5 0 q-4 -3 -6 -7 q-1 -2 1 -4 z"/>
      <text class="contact-text" x="124" y="520">(626) 555-0148</text>
    </g>
    <g class="contact contact--address">
      <circle class="contact-badge__ring" cx="503" cy="510" r="27"/>
      <circle class="contact-badge__core" cx="503" cy="510" r="20"/>
      <path class="contact-badge__icon" d="M503 522 q-9 -10 -9 -16 a9 9 0 0 1 18 0 q0 6 -9 16 z"/>
      <circle class="contact-badge__icon--solid" cx="503" cy="506" r="3"/>
      <text class="contact-text" x="545" y="520">58 Corvallen, Irvine, CA 92741</text>
    </g>
    <g class="contact contact--email">
      <circle class="contact-badge__ring" cx="88" cy="574" r="27"/>
      <circle class="contact-badge__core" cx="88" cy="574" r="20"/>
      <rect class="contact-badge__icon" x="77" y="566" width="22" height="16" rx="1"/>
      <path class="contact-badge__icon" d="M77 567 l11 8 l11 -8"/>
      <text class="contact-text" x="124" y="584">dana.whitcombe@q7eng.com</text>
    </g>
    <g class="contact contact--web">
      <circle class="contact-badge__ring" cx="709" cy="574" r="27"/>
      <circle class="contact-badge__core" cx="709" cy="574" r="20"/>
      <circle class="contact-badge__icon" cx="709" cy="574" r="11"/>
      <ellipse class="contact-badge__icon" cx="709" cy="574" rx="5" ry="11"/>
      <line class="contact-badge__icon" x1="698" y1="574" x2="720" y2="574"/>
      <text class="contact-text" x="746" y="584">www.q7eng.com</text>
    </g>
  </svg>

</main>
</body>
</html>
```